Business card design needed

We are a boutique law firm within the Melbourne CBD.

You will need to upload our company logo which is to go on the left hand side of the business card - we then have a Legal Guild of Carrowmere logo to go perhaps on the bottom right hand side (color)

On the back we would like the website details

www.hartwellsolicitors.com.au - with a small logo
Updates

Thank you designers for all your great submissions.  Just going through the designs and we will choose one within the next couple of days.

Kind Regards
Hartwells Solicitors Pty Ltd

Industry/Entity Type

Boutique

Contact Information for Business Card

Dominic Hartwell
Principal
Level 6, 47 Penrose Street
Melbourne VIC Australia 3000
T+61 3 9555 0142 F+61 3 9555 0187
dominic@hartwellsolicitors.com.au
M 0491 570 156

```html
<!DOCTYPE html>
<html lang="en">
<head>
<meta charset="utf-8">
<title>Hartwells Solicitors – Business Card</title>
<link rel="stylesheet" href="https://fonts.googleapis.com/css2?family=Arimo:wght@400;700&display=swap">
<style>
  :root {
    --ink: #0d0d0d;
    --paper: #ffffff;
    --stage: #e8e8e8;
    --muted: #d9d9d9;
    --guild-blue: #3a8fc9;
    --guild-navy: #1c2a44;
  }
  * { box-sizing: border-box; margin: 0; padding: 0; }
  html, body {
    width: 1200px; height: 900px; overflow: hidden;
    background: var(--stage);
    font-family: "Arimo", Arial, sans-serif;
  }
  .stage {
    width: 1200px; height: 900px;
    display: flex; align-items: center; justify-content: center; gap: 70px;
  }
  .card { box-shadow: 0 10px 24px rgba(0,0,0,.18); position: relative; overflow: hidden; }

  /* Back of card */
  .card-back {
    width: 540px; height: 310px; background: var(--ink); color: var(--paper);
    display: flex; flex-direction: column; align-items: center; justify-content: center; gap: 26px;
  }
  .brand { display: flex; align-items: center; gap: 12px; }
  .brand-square { width: 42px; height: 42px; background: var(--paper); }
  .brand-name { font-weight: 700; font-size: 34px; letter-spacing: .5px; color: var(--paper); }
  .back-url { font-weight: 700; font-size: 17px; letter-spacing: .2px; }

  /* Front of card */
  .card-front {
    width: 330px; height: 540px; background: var(--ink); color: var(--paper);
    display: flex; flex-direction: column;
  }
  .front-main { flex: 1; position: relative; padding: 28px 26px; }
  .front-brand { display: flex; align-items: center; gap: 10px; }
  .front-brand .brand-square { width: 30px; height: 30px; }
  .front-brand .brand-name { font-size: 26px; }
  .contact {
    position: absolute; right: 26px; bottom: 34px; text-align: right;
    font-size: 13px; line-height: 1.45;
  }
  .contact-name { font-weight: 700; font-size: 22px; margin-bottom: 4px; }
  .contact-role { margin-bottom: 10px; }
  .contact-email { margin-top: 10px; }
  .front-band {
    height: 118px; background: var(--paper); color: var(--ink);
    display: flex; align-items: center; justify-content: space-between; padding: 0 22px 0 26px;
  }
  .firm { font-size: 13.5px; line-height: 1.45; }
  .firm-name { font-weight: 700; font-size: 15px; }
  .guild-badge { width: 54px; height: 54px; flex: none; }
</style>
</head>
<body>
<main class="stage">
  <section class="card card-back" aria-label="Card back">
    <div class="brand">
      <span class="brand-square"></span>
      <span class="brand-name">Hartwells</span>
    </div>
    <p class="back-url">www.hartwellsolicitors.com.au</p>
  </section>

  <section class="card card-front" aria-label="Card front">
    <div class="front-main">
      <div class="front-brand">
        <span class="brand-square"></span>
        <span class="brand-name">Hartwells</span>
      </div>
      <div class="contact">
        <p class="contact-name">Dominic Hartwell</p>
        <p class="contact-role">Principal</p>
        <p>tel: +61 3 9555 0142</p>
        <p>fax: +61 3 9555 0187</p>
        <p>mob: 0491 570 156</p>
        <p class="contact-email">dominic@hartwellsolicitors.com.au</p>
      </div>
    </div>
    <div class="front-band">
      <div class="firm">
        <p class="firm-name">Hartwells Solicitors Pty Ltd</p>
        <p>Level 6, 47 Penrose Street</p>
        <p>Melbourne VIC 3000 Australia</p>
      </div>
      <svg class="guild-badge" viewBox="0 0 54 54" role="img" aria-label="Legal Guild of Carrowmere accreditation badge">
        <circle cx="27" cy="27" r="25" fill="var(--paper)" stroke="var(--guild-navy)" stroke-width="2"/>
        <circle cx="27" cy="27" r="15" fill="var(--guild-blue)"/>
      </svg>
    </div>
  </section>
</main>
</body>
</html>
```